Medical Clinic Website - New Private Clinic

We have a basic design for a website. Would like it developed in WORDPRESS. the attached JPG shows the page basic design.

Colours and overall design to be similar

MUST BE WORD PRESS and must allow our company to edit at later date. Images must be licenced for use.

The text to be included is:

Target Market(s)

Medical or GP clinic patients

Industry/Entity Type

Medical

Coding

Coded - Design and coding required

Number of Pages Required

1 page

Colors

Designer to choose colors to be used in the design.

Requirements
Must have
• WORDPRESS and use the attached jpg as a design guide.
• Must be able to allow me to insert link to "ember quill" in the top LEFT CORNER. a button or similar. The ember quill designers will help us with this, but it must have the space

```html
<!DOCTYPE html>
<html lang="en">
<head>
<meta charset="utf-8">
<title>Westgate Lane GP</title>
<link rel="stylesheet" href="https://fonts.googleapis.com/css2?family=Exo+2:wght@400;500;600&family=Open+Sans:wght@400;600;700&display=swap">
<style>
:root{
  --frame:#6e6e6e;
  --white:#ffffff;
  --green:#8dc21f;
  --green-soft:#b5d56a;
  --blue:#1a9ae0;
  --blue-deep:#0a6fc0;
  --blue-text:#2a8fd6;
  --ink:#3a3a3a;
  --grey-text:#5b6064;
  --panel:#dfe2e5;
  --field:#e7eef0;
}
*{box-sizing:border-box;margin:0;padding:0}
html,body{width:1200px;height:3158px;overflow:hidden;background:var(--frame)}
body{position:relative;font-family:"Open Sans",sans-serif;color:var(--ink)}
.page{position:absolute;left:74px;top:63px;width:1046px;height:3023px;background:var(--white);overflow:hidden}
.abs{position:absolute}
.heading{font-family:"Exo 2",sans-serif;font-weight:400}

/* header */
.site-header{left:0;top:0;width:1046px;height:118px;background:var(--white)}
.partner-link{left:73px;top:38px;width:181px;height:44px;border:2px solid #9aa3a8;color:var(--blue-text);font-family:"Exo 2",sans-serif;font-size:21px;display:flex;align-items:center;justify-content:center;text-transform:uppercase;letter-spacing:.5px}
.brand{left:380px;top:40px;width:290px;text-align:center;font-family:"Exo 2",sans-serif;font-size:28px;font-weight:500;color:var(--blue-deep);display:flex;align-items:center;justify-content:center;gap:10px}
.brand-mark{width:14px;height:14px;background:var(--green)}
.header-phone{left:800px;top:42px;font-family:"Exo 2",sans-serif;font-size:26px;color:var(--blue-text);display:flex;align-items:center;gap:12px}

/* nav */
.main-nav{left:0;top:118px;width:1046px;height:61px;background:var(--green);display:flex;align-items:center;padding-left:73px;gap:16px}
.main-nav a{color:var(--white);text-decoration:none;font-family:"Exo 2",sans-serif;font-size:20px}

/* hero */
.hero-visual{left:0;top:179px;width:1046px;height:368px;background:linear-gradient(100deg,#d8e9f7 0%,#7dbdf0 35%,#1b8fe3 60%,#9ccff5 100%)}
.cta-band{left:115px;top:491px;width:864px;height:115px}
.cta-small{left:168px;top:528px;color:var(--white);font-family:"Exo 2",sans-serif;font-size:15px;font-weight:600;letter-spacing:.5px}
.cta-big{left:168px;top:550px;color:var(--white);font-family:"Exo 2",sans-serif;font-size:21px;font-weight:600;letter-spacing:.5px}
.cta-button{left:625px;top:528px;width:252px;height:41px;border:2px solid var(--white);border-radius:21px;color:var(--white);font-family:"Exo 2",sans-serif;font-size:15px;font-weight:600;display:flex;align-items:center;justify-content:center;letter-spacing:.5px}

/* different */
.different{left:0;top:547px;width:1046px;height:659px;background:linear-gradient(90deg,#e4e6e8,#d7dadd)}
.doctor-visual{left:558px;top:547px;width:488px;height:659px;background:linear-gradient(180deg,#cfd3d6 0%,#f4f5f6 45%,#e8ebee 100%)}
.different-title{left:73px;top:135px;font-size:34px;color:var(--blue-text)}
.different-copy{left:73px;top:180px;width:449px;font-size:16px;line-height:22px;color:var(--grey-text);text-align:justify}
.feature{display:flex;align-items:center;gap:14px}
.feature svg{width:46px;height:46px;flex:none}
.feature-text{font-family:"Exo 2",sans-serif;color:var(--blue-text);line-height:1.25}
.feature-text small{display:block;font-size:12px;text-transform:uppercase}
.feature-text span{display:block;font-size:16px;text-transform:uppercase}

/* services */
.services{left:0;top:1206px;width:1046px;height:628px;background:var(--blue)}
.services-title{left:0;top:56px;width:1046px;text-align:center;font-size:34px;color:var(--white)}
.service{width:260px;text-align:center;color:var(--white);font-size:16px;font-weight:700;line-height:20px}
.service svg{display:block;margin:0 auto 6px;width:50px;height:50px}

/* appointment */
.appointment{left:0;top:1834px;width:1046px;height:726px;background:var(--green-soft)}
.form-card{left:75px;top:71px;width:447px;height:585px;background:var(--panel);border:5px solid var(--white);border-radius:14px}
.form-title{left:137px;top:96px;font-size:34px;color:var(--ink)}
.field{left:137px;width:322px;height:36px;background:var(--field);border:1px solid #d6dde0;color:#9aa2a6;font-size:13px;padding-left:14px;display:flex;align-items:center;text-transform:uppercase;letter-spacing:.3px}
.field.select{justify-content:space-between;padding-right:10px}
.field.area{height:80px;align-items:flex-start;padding-top:12px}
.submit{left:137px;top:570px;width:322px;height:38px;background:var(--green);color:var(--white);font-size:14px;font-weight:700;display:flex;align-items:center;justify-content:center;text-transform:uppercase}
.testimonials-title{left:574px;top:92px;font-size:46px;color:var(--ink)}
.quote-mark{left:574px;top:160px;font-family:Georgia,serif;font-size:86px;line-height:1;color:var(--white)}
.quote{left:640px;top:192px;width:326px;text-align:center;font-size:16px;line-height:22px;color:#2f3a20}
.quote-name{left:640px;top:428px;width:326px;text-align:center;font-size:20px;color:var(--ink)}
.quote-role{left:640px;top:455px;width:326px;text-align:center;font-size:15px;color:#3a4a2a}
.dots{left:750px;top:513px;display:flex;gap:11px;align-items:center}
.dots i{width:10px;height:10px;border-radius:50%;background:var(--white)}
.dots i.on{width:18px;height:18px;border:3px solid var(--white);background:#2c7a4a}

/* footer */
.site-footer{left:0;top:2560px;width:1046px;height:463px;background:linear-gradient(160deg,#8fb59a 0%,#6f9c7d 45%,#5e8e70 100%)}
.f-label{font-size:14px;color:var(--white);text-transform:uppercase}
.f-value{font-family:"Exo 2",sans-serif;font-size:29px;color:var(--white);line-height:36px}
.to-top{left:928px;top:362px;width:42px;height:42px;background:var(--white);border:2px solid #dfe7e2;display:flex;align-items:center;justify-content:center}
.copyright{left:0;top:418px;width:1046px;text-align:center;font-size:12px;color:var(--white)}
</style>
</head>
<body>
<main class="page">

  <header class="site-header abs">
    <a class="partner-link abs">Ember Quill</a>
    <div class="brand abs"><span class="brand-mark"></span>Westgate Lane GP</div>
    <div class="header-phone abs">
      <svg width="22" height="22" viewBox="0 0 24 24" fill="none" stroke="#8a9399" stroke-width="2"><path d="M5 3h4l2 5-3 2a12 12 0 0 0 6 6l2-3 5 2v4a2 2 0 0 1-2 2A17 17 0 0 1 3 5a2 2 0 0 1 2-2z"/></svg>
      6120 4937
    </div>
  </header>

  <nav class="main-nav abs">
    <a>HOME</a><a>ABOUT</a><a>SERVICES</a><a>CONTACT</a>
  </nav>

  <div class="hero-visual abs" role="img" aria-label="Doctor holding a stethoscope beside a grid of blue medical hexagon icons"></div>

  <section class="different abs">
    <div class="different-title abs heading">What Makes Us Different</div>
    <p class="different-copy abs">Lorem ipsum dolor sit amet, consectetur adipiscing elit. Sed vitae lectus pellentesque, condimentum leo ac, interdum orci. Morbi tristique ipsum nec convallis lobortis. Suspendisse justo nisi, dictum nec mattis eu, lobortis eget elit.</p>

    <div class="feature abs" style="left:84px;top:330px">
      <svg viewBox="0 0 48 48" fill="none" stroke="#2a8fd6" stroke-width="2.5"><circle cx="20" cy="18" r="8"/><path d="M6 42c0-8 6-13 14-13s14 5 14 13z"/><circle cx="36" cy="12" r="7"/><path d="M36 8v8M32 12h8"/></svg>
      <div class="feature-text"><small>Free</small><span>Consultation</span></div>
    </div>
    <div class="feature abs" style="left:320px;top:330px">
      <svg viewBox="0 0 48 48" fill="none" stroke="#2a8fd6" stroke-width="2.5"><circle cx="18" cy="16" r="8"/><path d="M4 42c0-8 6-13 14-13s14 5 14 13z"/><circle cx="32" cy="18" r="7"/><path d="M30 42h14c0-7-4-11-10-12"/></svg>
      <div class="feature-text"><small>Qualified</small><span>Doctors</span></div>
    </div>
    <div class="feature abs" style="left:84px;top:432px">
      <svg viewBox="0 0 48 48" fill="none" stroke="#2a8fd6" stroke-width="2.5"><rect x="8" y="10" width="32" height="22" rx="2"/><path d="M3 38h42l-3-6H6z"/></svg>
      <div class="feature-text"><small>Professional</small><span>Staff</span></div>
    </div>
    <div class="feature abs" style="left:320px;top:432px">
      <svg viewBox="0 0 48 48" fill="none" stroke="#2a8fd6" stroke-width="2.5"><circle cx="24" cy="26" r="15"/><path d="M24 17v9l6 4M8 12l6-6M40 12l-6-6"/></svg>
      <div class="feature-text"><small>24x7</small><span>Opened</span></div>
    </div>
    <div class="feature abs" style="left:84px;top:535px">
      <svg viewBox="0 0 48 48" fill="none" stroke="#2a8fd6" stroke-width="2.5"><rect x="6" y="12" width="32" height="20" rx="2"/><rect x="11" y="18" width="32" height="20" rx="2"/><path d="M11 24h32"/></svg>
      <div class="feature-text"><small>Affordable</small><span>Prices</span></div>
    </div>
    <div class="feature abs" style="left:320px;top:535px">
      <svg viewBox="0 0 48 48" fill="none" stroke="#2a8fd6" stroke-width="2.5"><rect x="5" y="22" width="8" height="18"/><path d="M13 24l8-10 2-8c4 0 5 4 4 9h12a3 3 0 0 1 0 6 3 3 0 0 1-1 6 3 3 0 0 1-2 5 3 3 0 0 1-3 4H13"/></svg>
      <div class="feature-text"><small>~100000</small><span>Happy Clients</span></div>
    </div>
  </section>
  <div class="doctor-visual abs" role="img" aria-label="Doctor in a white coat with a stethoscope holding a blue clipboard"></div>

  <svg class="cta-band abs" viewBox="0 0 864 115" aria-hidden="true"><polygon points="40,0 824,0 864,57.5 824,115 40,115 0,57.5" fill="#8dc21f"/></svg>
  <div class="cta-small abs">IF YOU NEED A DOCTOR ?</div>
  <div class="cta-big abs">MAKE AN APPOINTMENT NOW !</div>
  <a class="cta-button abs">GET AN APPOINTMENT</a>

  <section class="services abs">
    <div class="services-title abs heading">What We Do</div>

    <div class="service abs" style="left:129px;top:144px">
      <svg viewBox="0 0 50 50"><path d="M23 8v16M27 8v16" stroke="#3a3a3a" stroke-width="2.5"/><path d="M22 18c-8-4-14 6-14 18 0 6 6 8 14 4z M28 18c8-4 14 6 14 18 0 6-6 8-14 4z" fill="#f4b3a8" stroke="#3a3a3a" stroke-width="2"/></svg>
      Chronic Disease<br>Management
    </div>
    <div class="service abs" style="left:396px;top:144px">
      <svg viewBox="0 0 50 50"><rect x="17" y="5" width="16" height="8" fill="#f3a43c" stroke="#3a3a3a" stroke-width="2"/><rect x="13" y="13" width="24" height="32" rx="3" fill="#f4d7c9" stroke="#3a3a3a" stroke-width="2"/><path d="M25 22v14M18 29h14" stroke="#e04848" stroke-width="4"/></svg>
      Dermatology &amp;<br>Wound Management
    </div>
    <div class="service abs" style="left:661px;top:144px">
      <svg viewBox="0 0 50 50"><path d="M25 44S5 31 5 17A10 10 0 0 1 25 12a10 10 0 0 1 20 5c0 14-20 27-20 27z" fill="#ef5a5a" stroke="#3a3a3a" stroke-width="2"/><path d="M8 26h10l4-8 5 14 4-6h11" fill="none" stroke="#fff" stroke-width="2.5"/></svg>
      Health Promotion<br>Activities
    </div>

    <div class="service abs" style="left:129px;top:318px">
      <svg viewBox="0 0 50 50"><path d="M10 40l24-24 6 6-24 24z" fill="#d9e4ea" stroke="#3a3a3a" stroke-width="2"/><path d="M4 46l8-8M34 10l8 8M38 6l8 8" stroke="#3a3a3a" stroke-width="2.5"/><path d="M14 38l18-18" stroke="#e04848" stroke-width="3"/></svg>
      Immunizations
    </div>
    <div class="service abs" style="left:396px;top:318px">
      <svg viewBox="0 0 50 50"><path d="M10 26c-4-12 8-20 18-16 10-2 16 8 12 16 2 6-4 10-10 8l-4 6h-6v-6c-6 0-12-2-10-8z" fill="#f6b3b0" stroke="#3a3a3a" stroke-width="2"/><path d="M20 18c4 0 4 6 8 4M28 14c2 4 8 2 8 8" fill="none" stroke="#3a3a3a" stroke-width="2"/></svg>
      Mental Health
    </div>
    <div class="service abs" style="left:661px;top:318px">
      <svg viewBox="0 0 50 50"><rect x="12" y="6" width="26" height="40" fill="#f3c28a" stroke="#3a3a3a" stroke-width="2"/><g fill="#3a3a3a"><rect x="17" y="12" width="5" height="5"/><rect x="28" y="12" width="5" height="5"/><rect x="17" y="22" width="5" height="5"/><rect x="28" y="22" width="5" height="5"/></g><rect x="21" y="34" width="8" height="12" fill="#e04848"/></svg>
      Work Related<br>Injury Management
    </div>

    <div class="service abs" style="left:129px;top:485px">
      <svg viewBox="0 0 50 50"><rect x="4" y="16" width="30" height="20" fill="#ffffff" stroke="#3a3a3a" stroke-width="2"/><path d="M34 22h8l5 7v7H34z" fill="#e04848" stroke="#3a3a3a" stroke-width="2"/><path d="M19 20v12M13 26h12" stroke="#e04848" stroke-width="3"/><circle cx="12" cy="38" r="4" fill="#3a3a3a"/><circle cx="38" cy="38" r="4" fill="#3a3a3a"/></svg>
      Accident Assessment
    </div>
    <div class="service abs" style="left:396px;top:485px">
      <svg viewBox="0 0 50 50"><rect x="8" y="40" width="34" height="6" fill="#3a3a3a"/><path d="M16 8l10 4-8 22" fill="none" stroke="#3a3a3a" stroke-width="4"/><path d="M28 18h10v22H28z" fill="#e04848" stroke="#3a3a3a" stroke-width="2"/></svg>
      Diagonstic Services
    </div>
    <div class="service abs" style="left:661px;top:485px">
      <svg viewBox="0 0 50 50"><circle cx="24" cy="8" r="5" fill="#f3c28a" stroke="#3a3a3a" stroke-width="2"/><path d="M24 14v14h10l4 12" fill="none" stroke="#3a3a3a" stroke-width="4"/><circle cx="22" cy="36" r="9" fill="none" stroke="#9aa2a6" stroke-width="3"/></svg>
      Physiotherapy
    </div>
  </section>

  <section class="appointment abs">
    <div class="form-card abs"></div>
    <div class="form-title abs heading">Get An Appointment</div>
    <div class="field select abs" style="top:176px">Select Department
      <svg width="12" height="8" viewBox="0 0 12 8"><path d="M1 1l5 5 5-5" fill="none" stroke="#9aa2a6" stroke-width="1.5"/></svg>
    </div>
    <div class="field abs" style="top:245px">Full Name</div>
    <div class="field abs" style="top:313px">Phone Number</div>
    <div class="field abs" style="top:382px">Email Address</div>
    <div class="field area abs" style="top:451px">Problem</div>
    <a class="submit abs">Make An Appointment</a>

    <div class="testimonials-title abs heading">Testimonials</div>
    <div class="quote-mark abs">&ldquo;</div>
    <p class="quote abs">Nemo enim ipsam voluptatem quia voluptas sit aspernatur aut odit aut fugit, sed quia consequuntur magni dolores eos qui ratione voluptatem sequi nesciunt. Neque porro quisquam est, qui dolorem ipsum quia dolor sit amet, consectetur, adipisci velit, sed quia non numquam eius modi tempora incidunt ut labore.</p>
    <div class="quote-name abs">Margot Ellery</div>
    <div class="quote-role abs">Blood Patient</div>
    <div class="dots abs"><i></i><i></i><i class="on"></i><i></i><i></i></div>
  </section>

  <footer class="site-footer abs" role="img" aria-label="Softly blurred clinic reception interior in green tones">
    <div class="abs" style="left:73px;top:70px">
      <div class="f-label">Emergency Cases</div>
      <div class="f-value">6120 4937</div>
    </div>
    <div class="abs" style="left:486px;top:70px">
      <div class="f-label">Online Consultation</div>
      <div class="f-value">reception@westgatelanegp.com.au</div>
    </div>
    <div class="abs" style="left:73px;top:182px">
      <div class="f-label">Locate Us</div>
      <div class="f-value">EAST HAVEN<br>AUSTRALIA</div>
    </div>
    <div class="to-top abs">
      <svg width="16" height="12" viewBox="0 0 16 12"><polygon points="8,0 16,12 0,12" fill="#1f7a45"/></svg>
    </div>
    <div class="copyright abs">Copyright Westgate Lane GP, 2017</div>
  </footer>

</main>
</body>
</html>
```